Roofing Company Modern look

I want a modern and sophisticated look for our roofing business.

Our address is :

4276 Pellman Crossing Rd
Orlando, Fl 32825

(407)-583-2716

www.SummitcrestShinglesFl.com

I also want to make sure on the back there is a spot to put
Project Manager Name :

Number:

Because the cards will be used by all sales people

Project Manager Name :

Also there are accreditation we have logos are uploaded here as well that I would like maybe on the back of card as well

I also want to highlight our special attributions or trades:

Residential & Commercial
Fully Insured
License # CCC4872196
Insurance Claims
Serving Central Florida Since 1992
Free Estimates

Contact Information for Business Card

Our address is :

4276 Pellman Crossing Rd
Orlando, Fl 32825

(407)-583-2716

Project Manager Name :

Residential & Commercial
Fully Insured
License # CCC4872196
Insurance Claims
Free Estimates

Font styles to use
Serif
Sans Serif

Colors
3176b5

Requirements
Must have
• Must have royal blue like my logo grey and black are the colors I like

```html
<!DOCTYPE html>
<html lang="en">
<head>
<meta charset="utf-8">
<title>Summitcrest Roofing &amp; Gutters – Business Card</title>
<link rel="stylesheet" href="https://fonts.googleapis.com/css2?family=Montserrat:wght@400;500;600&display=swap">
<style>
  :root {
    --royal-blue: #1f77c4;
    --brand-blue: #3176b5;
    --ink: #4a4a4a;
    --dark-grey: #555;
    --black: #0b0b0b;
    --stage: #2b2b2b;
    --white: #ffffff;
    --paper: #f6f7f8;
    --badge-navy: #1d3250;
    --badge-blue: #1b5e94;
    --badge-red: #d22730;
    --badge-grey: #8a8f94;
  }
  * { box-sizing: border-box; margin: 0; padding: 0; }
  html, body { width: 1200px; height: 1192px; overflow: hidden; }
  body {
    background: var(--stage);
    font-family: "Montserrat", sans-serif;
    position: relative;
  }
  .card {
    position: absolute;
    left: 209px;
    width: 782px;
    height: 448px;
    border-radius: 14px;
    overflow: hidden;
  }
  /* Front */
  .card-front { top: 130px; background: var(--white); }
  .front-brand {
    position: absolute; left: 50px; top: 250px;
    display: flex; align-items: center; gap: 12px;
  }
  .brand-dot {
    width: 20px; height: 20px; border-radius: 50%;
    background: var(--royal-blue);
  }
  .brand-name {
    color: var(--royal-blue);
    font-weight: 600;
    font-size: 20px;
    letter-spacing: 0.5px;
    line-height: 1.2;
  }
  .front-brand { top: 140px; }
  .person { position: absolute; left: 50px; top: 244px; }
  .person-name { font-size: 25px; font-weight: 500; color: var(--ink); line-height: 1.1; }
  .person-name .first { color: var(--royal-blue); }
  .person-role { font-size: 19px; color: var(--dark-grey); margin-top: 4px; }
  .contact-row {
    position: absolute; left: 50px; top: 324px;
    display: flex; align-items: flex-end; gap: 14px;
  }
  .contact-list { list-style: none; }
  .contact-list li {
    display: flex; align-items: center; gap: 8px;
    font-size: 18px; color: var(--ink); line-height: 26px;
  }
  .contact-list svg { width: 14px; height: 14px; fill: var(--royal-blue); flex: none; }
  .address {
    border-left: 2px solid var(--royal-blue);
    padding-left: 12px;
    font-size: 18px; color: var(--dark-grey); line-height: 24px;
  }
  /* Back */
  .card-back { top: 614px; background: var(--paper); }
  .back-top {
    position: absolute; left: 0; top: 0; width: 100%; height: 332px;
    background: var(--black);
    border-bottom: 3px solid var(--royal-blue);
  }
  .back-brand {
    position: absolute; left: 0; right: 0; top: 110px;
    display: flex; justify-content: center; align-items: center; gap: 18px;
  }
  .back-brand .brand-dot { width: 34px; height: 34px; }
  .back-brand .brand-name { font-size: 34px; line-height: 1.15; }
  .back-url {
    position: absolute; left: 0; right: 0; top: 290px;
    text-align: center; color: var(--white);
    font-size: 21px; letter-spacing: 1px;
  }
  .partners-label {
    position: absolute; left: 50%; top: 320px; transform: translateX(-50%);
    background: var(--royal-blue); color: var(--white);
    font-size: 19px; padding: 0 12px; height: 24px; line-height: 24px;
    border-radius: 12px; white-space: nowrap;
  }
  .badges {
    position: absolute; left: 0; top: 360px; width: 100%; height: 80px;
  }
  .badge { position: absolute; }
  .badge-listing { left: 166px; top: 4px; width: 52px; height: 68px; border-radius: 4px; background: var(--badge-blue); }
  .badge-applicator { left: 256px; top: 2px; width: 74px; height: 64px; }
  .badge-contractor { left: 368px; top: 14px; width: 142px; height: 40px; background: var(--white); border: 2px solid var(--badge-red); }
  .badge-approved { left: 541px; top: 2px; width: 70px; height: 70px; border-radius: 50%; background: var(--badge-grey); }
</style>
</head>
<body>

<section class="card card-front" aria-label="Business card front">
  <div class="front-brand">
    <span class="brand-dot"></span>
    <div class="brand-name">SUMMITCREST<br>ROOFING &amp; GUTTERS INC.</div>
  </div>

  <div class="person">
    <p class="person-name"><span class="first">Daniel</span> Okafor</p>
    <p class="person-role">Project Manager</p>
  </div>

  <div class="contact-row">
    <ul class="contact-list">
      <li>
        <svg viewBox="0 0 24 24" aria-hidden="true"><path d="M6.6 10.8a15.1 15.1 0 0 0 6.6 6.6l2.2-2.2c.3-.3.7-.4 1-.2 1.1.4 2.3.6 3.6.6.6 0 1 .4 1 1V20c0 .6-.4 1-1 1A17 17 0 0 1 3 4c0-.6.4-1 1-1h3.5c.6 0 1 .4 1 1 0 1.3.2 2.5.6 3.6.1.3 0 .7-.2 1z"/></svg>
        (407)-583-2716
      </li>
      <li>
        <svg viewBox="0 0 24 24" aria-hidden="true"><path d="M2 5h20v14H2z M2 5l10 8 10-8" fill="none" stroke="#1f77c4" stroke-width="2.4"/></svg>
        SummitcrestShinglesFl@gmail.com
      </li>
      <li>
        <svg viewBox="0 0 24 24" aria-hidden="true"><circle cx="12" cy="12" r="10"/></svg>
        www.SummitcrestShinglesFl.com
      </li>
    </ul>
    <address class="address" style="font-style:normal">
      4276 Pellman Crossing Rd<br>Orlando, Fl 32825
    </address>
  </div>
</section>

<section class="card card-back" aria-label="Business card back">
  <div class="back-top">
    <div class="back-brand">
      <span class="brand-dot"></span>
      <div class="brand-name">SUMMITCREST<br>ROOFING &amp; GUTTERS LLC.</div>
    </div>
    <p class="back-url">www.summitcrestshinglesfl.com</p>
  </div>
  <p class="partners-label">Our Accreditations &amp; Partners</p>
  <div class="badges">
    <div class="badge badge-listing" role="img" aria-label="Business accreditation badge"></div>
    <svg class="badge badge-applicator" viewBox="0 0 74 64" role="img" aria-label="Shingle applicator certification badge">
      <polygon points="37,0 74,20 74,44 37,64 0,44 0,20" fill="var(--badge-navy)"/>
    </svg>
    <div class="badge badge-contractor" role="img" aria-label="Authorized roofing contractor badge"></div>
    <div class="badge badge-approved" role="img" aria-label="Screened and approved listing badge"></div>
  </div>
</section>

</body>
</html>
```